Simple Business Card Design for Foodie

Job:

Make a very simple, minimalist business card design with my details including adjusted logo. One side to be white (with logo & text). Other side to be yellow - try plain or with logo (or part of logo eg Z). Need business card to have continuity with website.

Logo:
Our logo is made from a free download font website:
http://www.glyphbarn.net/search.php?q=rubber
but the spacing/kerning needs correcting/adjusting as the font spaces unevenly between letters (see attached files). Need logo to be very crisp/sharp when printed.

Printing:
We will be using Parcly.com so the design needs to conform to their requirements, see here:

http://uk.parcly.com/products/velin/business-cards.html (scroll down for dimensions and guidelines)

Design:

must say "plant-based food consulting" underneath logo or somewhere
no address needed in contact section
sharp corners (not rounded)
one side white, one side yellow

name: Marisol Quenby
1xmobile number: +44 7700 900431
1xtwiiter: @quillcounsel
website address www.greenplatehub.example
email address quill@greenplatehub.example

Should be easy quick job, prompt + detailed feedback given, am online in UK 9am-10pm for next 3 days. Website is www.greenplatehub.example

Must have
• The logo must be corrected. The kerning is not right.

Please use a warm-grey for text

Please submit in matt format, we will be printing matt finish.

Should not have
• Avoid using banners or curvy highlights

Please avoid using black

Please avoid submitting in gloss finish

```html
<!DOCTYPE html>
<html lang="en">
<head>
<meta charset="utf-8">
<title>Quill business card</title>
<link rel="stylesheet" href="https://fonts.googleapis.com/css2?family=Tinos:ital,wght@0,400;0,700;1,400&display=swap">
<style>
  :root {
    --bg: #8d8d8d;
    --card-white: #ffffff;
    --card-yellow: #fff95e;
    --brand-yellow: #fff55a;
    --icon-yellow: #e8de3a;
    --ink: #4a4541;
    --shadow: rgba(0,0,0,0.28);
  }
  * { box-sizing: border-box; margin: 0; padding: 0; }
  html, body { width: 1200px; height: 960px; overflow: hidden; }
  body {
    background: var(--bg);
    font-family: "Tinos", "Times New Roman", serif;
    position: relative;
  }
  .card {
    position: absolute;
    left: 220px;
    width: 760px;
    height: 420px;
    box-shadow: 0 10px 24px var(--shadow);
    overflow: hidden;
  }
  .wordmark {
    font-family: "Tinos", "Times New Roman", serif;
    font-weight: 700;
    color: var(--brand-yellow);
    letter-spacing: 8px;
    line-height: 1;
    white-space: nowrap;
  }

  /* Yellow side */
  .card--back { top: 40px; background: var(--card-yellow); }
  .card--back .logo-panel {
    position: absolute;
    left: 160px; top: 80px;
    width: 440px; height: 180px;
    background: var(--card-white);
    display: flex; align-items: center; justify-content: center;
  }
  .card--back .wordmark { font-size: 92px; padding-left: 8px; }
  .card--back .url-band {
    position: absolute;
    left: 0; right: 0; top: 300px; height: 56px;
    background: var(--card-white);
    display: flex; align-items: center; justify-content: center;
  }
  .card--back .url-band span {
    font-weight: 700; font-size: 17px;
    letter-spacing: 4px; color: var(--ink);
  }

  /* White side */
  .card--front { top: 500px; background: var(--card-white); }
  .card--front .wordmark {
    position: absolute; left: 230px; top: 30px;
    font-size: 112px;
  }
  .card--front .tagline {
    position: absolute; left: 236px; top: 146px;
    font-size: 17px; letter-spacing: 3px;
    color: var(--ink);
  }
  .card--front .person-name {
    position: absolute; left: 60px; top: 206px;
    font-size: 22px; font-weight: 700;
    color: var(--ink);
  }
  .contact-list {
    position: absolute; left: 60px; top: 246px;
    list-style: none;
  }
  .contact-list li {
    display: flex; align-items: center; gap: 14px;
    font-size: 20px; color: var(--ink);
    height: 34px;
  }
  .contact-list svg { width: 22px; height: 22px; flex: none; }
</style>
</head>
<body>
  <section class="card card--back" aria-label="Yellow side of the card">
    <div class="logo-panel"><span class="wordmark">QUILL</span></div>
    <div class="url-band"><span>www.greenplatehub.example</span></div>
  </section>

  <section class="card card--front" aria-label="White side of the card">
    <span class="wordmark">QUILL</span>
    <p class="tagline">plant-based food consulting</p>
    <p class="person-name">Marisol Quenby</p>
    <ul class="contact-list">
      <li>
        <svg viewBox="0 0 24 24" aria-hidden="true"><path d="M6 3l3 0 2 5-2 2c1 2 3 4 5 5l2-2 5 2 0 3c0 2-2 3-4 3C10 21 3 14 3 7c0-2 1-4 3-4z" fill="none" stroke="var(--icon-yellow)" stroke-width="2" stroke-linejoin="round"/></svg>
        <span>+44 7700 900431</span>
      </li>
      <li>
        <svg viewBox="0 0 24 24" aria-hidden="true"><circle cx="12" cy="12" r="8" fill="none" stroke="var(--icon-yellow)" stroke-width="2.4"/></svg>
        <span>@quillcounsel</span>
      </li>
      <li>
        <svg viewBox="0 0 24 24" aria-hidden="true"><path d="M2 12L12 3l10 9M5 10v10h5v-6h4v6h5V10" fill="none" stroke="var(--icon-yellow)" stroke-width="2.2" stroke-linejoin="round"/></svg>
        <span>www.greenplatehub.example</span>
      </li>
      <li>
        <svg viewBox="0 0 24 24" aria-hidden="true"><circle cx="12" cy="12" r="4" fill="none" stroke="var(--icon-yellow)" stroke-width="2.4"/><path d="M16 8v5c0 2 4 2 4-1a8 8 0 1 0-3 6" fill="none" stroke="var(--icon-yellow)" stroke-width="2.4" stroke-linecap="round"/></svg>
        <span>quill@greenplatehub.example</span>
      </li>
    </ul>
  </section>
</body>
</html>
```